Website design for management consulting firm

We need a web design for a new consulting company based in Boston, MA called "Quillmoor Ridge Consulting." This webpage will be simple home page, with a "contact us" page, that describes the services of the consulting firm. The company provides strategic planning, business assessment, process re-designs, and other management consulting functions. I would like the website to look high-tech. A logo was already created via Artsy Hive.

Target Market(s)

Other business owners across a wide spectrum of industries - from IT to retail.

Industry/Entity Type

It Company

Number of Pages Required

3 page

Colors
0455a3
ffffff

Requirements
Must have
• Front page that provides generic text / overview of the firm. A "services" tab that describes consulting services. A "contact us" tab that provides either a form to contact us or just the contact email address of the company. info@quillmoorridgeconsulting.example

```html
<!DOCTYPE html>
<html lang="en">
<head>
<meta charset="UTF-8">
<title>Quillmoor Ridge Consulting</title>
<link href="https://fonts.googleapis.com/css2?family=Arimo:wght@400;700&family=Tinos&display=swap" rel="stylesheet">
<style>
  :root {
    --page-teal: #1fa596;
    --deep-blue: #045a82;
    --bright-teal: #12c2b1;
    --wave-teal: #2bb3a3;
    --title-teal: #22ad9d;
    --ink: #111111;
    --white: #ffffff;
  }
  * { box-sizing: border-box; margin: 0; padding: 0; }
  html, body { width: 1108px; height: 1200px; overflow: hidden; }
  body {
    background: var(--page-teal);
    font-family: "Tinos", "Times New Roman", serif;
    position: relative;
  }
  .site-header {
    position: absolute; left: 0; top: 0;
    width: 1108px; height: 245px;
    background: var(--white);
    display: flex; align-items: center;
  }
  .brand-panel {
    width: 227px; height: 245px;
    flex: none;
    background: linear-gradient(180deg, var(--deep-blue) 0%, var(--deep-blue) 62%, var(--wave-teal) 100%);
  }
  .brand-name {
    margin-left: 70px;
    font-family: "Arimo", Arial, sans-serif;
    font-weight: 700;
    font-size: 86px;
    line-height: 1.0;
    color: var(--ink);
    letter-spacing: -2px;
  }
  .main-nav {
    position: absolute; left: 0; top: 245px;
    width: 1108px; height: 85px;
    background: var(--deep-blue);
    display: flex; align-items: center; justify-content: space-between;
    padding: 0 14px 0 66px;
  }
  .main-nav a {
    color: var(--title-teal);
    font-size: 66px;
    text-decoration: none;
    line-height: 1;
  }
  .nav-divider {
    width: 18px; height: 18px;
    background: var(--white);
  }
  .services {
    position: absolute; left: 12px; top: 339px;
    display: grid;
    grid-template-columns: 537px 537px;
    grid-auto-rows: 203px;
    column-gap: 11px;
    row-gap: 14px;
  }
  .service-card {
    background: var(--deep-blue);
    display: flex;
    padding: 6px;
  }
  .service-image {
    width: 150px; height: 191px;
    background: var(--bright-teal);
    flex: none;
    display: flex; align-items: center; justify-content: center;
    text-align: center;
    font-family: "Arimo", Arial, sans-serif;
    font-weight: 400;
    font-size: 29px; line-height: 1.5;
    color: var(--ink);
  }
  .service-body { padding-left: 8px; overflow: hidden; }
  .service-title {
    font-weight: 400;
    font-size: 66px;
    line-height: 1;
    color: var(--title-teal);
    margin-top: -2px;
    white-space: nowrap;
  }
  .service-text {
    margin-top: 14px;
    font-size: 19.5px;
    line-height: 25.5px;
    color: var(--ink);
    padding-left: 4px;
    white-space: nowrap;
  }
</style>
</head>
<body>
  <header class="site-header">
    <div class="brand-panel" role="img" aria-label="Brand panel in deep blue fading to teal"></div>
    <div class="brand-name">Quillmoor Ridge<br>Consulting</div>
  </header>

  <nav class="main-nav">
    <a href="#">Home</a>
    <span class="nav-divider"></span>
    <a href="#">Services</a>
    <span class="nav-divider"></span>
    <a href="#">Contact Us</a>
  </nav>

  <main class="services">
    <article class="service-card"><div class="service-image" role="img" aria-label="Photo for strategic planning">Service<br>Image</div><div class="service-body"><h2 class="service-title">Strategy</h2><p class="service-text">Plans that set direction and clear goals,<br>built around the market you compete in,<br>with milestones your team can measure,<br>reviewed each quarter as plans evolve.</p></div></article>
    <article class="service-card"><div class="service-image" role="img" aria-label="Photo for business assessment">Service<br>Image</div><div class="service-body"><h2 class="service-title">Assessment</h2><p class="service-text">A full review of how your business runs,<br>from finances and staffing to systems,<br>with an honest view of strengths, gaps,<br>and the risks that need attention first.</p></div></article>
    <article class="service-card"><div class="service-image" role="img" aria-label="Photo for process redesign">Service<br>Image</div><div class="service-body"><h2 class="service-title">Redesign</h2><p class="service-text">We map the way work moves through teams,<br>remove the steps that slow delivery down,<br>and rebuild each process around results<br>your customers can see and feel quickly.</p></div></article>
    <article class="service-card"><div class="service-image" role="img" aria-label="Photo for operations consulting">Service<br>Image</div><div class="service-body"><h2 class="service-title">Operations</h2><p class="service-text">Daily operations tuned for steady output,<br>with clear roles, simple handoffs, and<br>reporting that shows where time is spent<br>so managers can act before issues grow.</p></div></article>
    <article class="service-card"><div class="service-image" role="img" aria-label="Photo for technology advice">Service<br>Image</div><div class="service-body"><h2 class="service-title">Technology</h2><p class="service-text">Guidance on choosing and rolling out IT,<br>from core platforms to small daily tools,<br>matched to your budget and your people,<br>with support through every launch phase.</p></div></article>
    <article class="service-card"><div class="service-image" role="img" aria-label="Photo for growth planning">Service<br>Image</div><div class="service-body"><h2 class="service-title">Growth</h2><p class="service-text">Routes to new customers and new markets,<br>backed by research into demand, pricing,<br>and the partners worth working alongside,<br>so expansion stays focused and funded.</p></div></article>
    <article class="service-card"><div class="service-image" role="img" aria-label="Photo for leadership coaching">Service<br>Image</div><div class="service-body"><h2 class="service-title">Leadership</h2><p class="service-text">Coaching for owners and senior managers,<br>covering decision making, delegation, and<br>the habits that keep teams aligned while<br>the company grows across new locations.</p></div></article>
    <article class="service-card"><div class="service-image" role="img" aria-label="Photo for change management">Service<br>Image</div><div class="service-body"><h2 class="service-title">Change</h2><p class="service-text">Support for major change in your company,<br>from mergers and new structures to new<br>systems, with plans for communication<br>that keep staff informed and on board.</p></div></article>
  </main>
</body>
</html>
```